Box Truck wrap for an insulation company

Full wrap design for a box truck.
The services we offer are

Target Market(s)

Homeowners

Industry/Entity Type

Home Improvement

Colors
acd136
0455a3

Requirements
Must have
• Lic# 3859160 (Small. Required by law)
559-318-2264 (large)
Www.Marlowheatworks.com
Logo (large)
We fix high utility bills

Insulation
Whole house fans
Insulation removal
Window film
Thermal imaging inspections
Solar
and more
Nice to have
• a blended collage of solar, insulation, and thermal imaging

```html
<!DOCTYPE html>
<html lang="en">
<head>
<meta charset="utf-8">
<title>Marlow Heatworks – Box Truck Wrap</title>
<link href="https://fonts.googleapis.com/css2?family=Michroma&family=Roboto:ital,wght@0,700;1,400;1,700&display=swap" rel="stylesheet">
<style>
  :root{
    --blue:#0455a3;
    --green:#acd136;
    --ink:#000;
    --paper:#fff;
    --photo-a:#6b4a36;
    --photo-b:#c9a3b8;
    --photo-c:#8a5a3c;
  }
  *{margin:0;padding:0;box-sizing:border-box}
  html,body{width:1200px;height:628px;overflow:hidden;background:var(--ink)}
  .canvas{position:relative;width:1200px;height:628px;background:var(--ink);font-family:"Roboto",Arial,sans-serif}
  .outlines{position:absolute;left:0;top:0}
  .swatch{position:absolute;width:35px;height:35px}
  .swatch--blue{background:var(--blue)}
  .swatch--green{background:var(--green)}
  .panel{position:absolute}
  .back-door{background:var(--paper);border:1px solid #d22;width:245px;height:206px}
  .side{width:510px;height:220px}
  .photo{position:absolute;left:0;top:0}
  .phone{position:absolute;transform:translateX(-50%);white-space:nowrap;font-weight:700;color:var(--blue);letter-spacing:.2px}
  .phone .area{color:var(--green)}
  .url{position:absolute;transform:translateX(-50%);white-space:nowrap;font-style:italic;color:var(--green)}
  .url b{color:var(--blue);font-weight:700}
  .tagline{position:absolute;transform:translateX(-50%);white-space:nowrap;font-style:italic;font-weight:700;color:var(--green)}
  .services{position:absolute;list-style:none;color:var(--blue);font-style:italic;font-size:7.5px}
  .services li{height:12px;line-height:12px;padding-left:7px;position:relative}
  .services li::before{content:"";position:absolute;left:0;top:4px;width:4px;height:4px;border-radius:50%;background:var(--green)}
  .services li.more::before{display:none}
  .brand{position:absolute;transform:translateX(-50%);white-space:nowrap;font-family:"Michroma",Arial,sans-serif;color:var(--blue);text-align:center;line-height:1.15}
  .brand-mark{position:absolute;transform:translateX(-50%);border-radius:50%;background:var(--green)}
  .badge{position:absolute;width:37px;height:24px;border-radius:3px;background:var(--blue)}
  .license{position:absolute;transform:translateX(-50%);white-space:nowrap;font-style:italic;font-weight:700;font-size:9px;color:var(--blue)}
</style>
</head>
<body>
<div class="canvas">

  <svg class="outlines" width="1200" height="628" viewBox="0 0 1200 628" aria-hidden="true">
    <path d="M453,35 H945 Q958,36 960,55 V72 H963 V254 L454,256 Z" fill="#fff" stroke="#d22" stroke-width="0.8"/>
    <path d="M970,150 L1025,151 L1071,186 L1109,219 L1160,228 L1171,242 L1164,261 L1167,280 L1137,280 Q1120,252 1096,262 Q1080,270 1081,280 L1075,290 L1066,312 L962,313 Z" fill="#fff" stroke="#d22" stroke-width="0.8"/>
    <path d="M983,163 L1040,163 L1066,192 L1066,220 L985,222 Q978,200 983,163 Z" fill="#000"/>
    <rect x="976" y="247" width="3" height="12" fill="#000"/>
    <path d="M771,320 H279 Q266,321 264,340 V357 H261 V539 L770,538 Z" fill="#fff" stroke="#d22" stroke-width="0.8"/>
    <path d="M254,433 L199,434 L153,469 L115,502 L64,511 L53,525 L60,544 L57,563 L87,563 Q104,535 128,545 Q144,553 143,563 L149,573 L158,595 L262,596 Z" fill="#fff" stroke="#d22" stroke-width="0.8"/>
    <path d="M241,446 L184,446 L158,475 L158,503 L239,505 Q246,483 241,446 Z" fill="#000"/>
    <rect x="245" y="530" width="3" height="12" fill="#000"/>
  </svg>

  <div class="swatch swatch--blue" style="left:100px;top:58px"></div>
  <div class="swatch swatch--green" style="left:100px;top:100px"></div>
  <div class="swatch swatch--blue" style="left:1071px;top:344px"></div>
  <div class="swatch swatch--green" style="left:1071px;top:386px"></div>

  <!-- rear door, services version -->
  <section class="panel back-door" style="left:157px;top:58px">
    <div class="brand-mark" style="left:70px;top:44px;width:34px;height:34px"></div>
    <div class="brand" style="left:70px;top:84px;font-size:10.5px">MARLOW<br>HEATWORKS</div>
    <ul class="services" style="left:134px;top:40px">
      <li>Insulation</li><li>Whole house fans</li><li>Window film</li><li>Insulation Removal</li><li>Thermal Imaging Inspections</li><li>Solar</li><li class="more">And more</li>
    </ul>
    <div class="tagline" style="left:85px;top:124px;font-size:9px">We fix high utility bills</div>
    <div class="phone" style="left:85px;top:143px;font-size:18px"><span class="area">(559)</span> 318-2264</div>
    <div class="url" style="left:85px;top:165px;font-size:8.5px">www.<b>MarlowHeatworks</b>.com</div>
    <div class="badge" style="left:193px;top:150px" aria-label="Rating badge"></div>
  </section>

  <!-- driver side box, photo left -->
  <section class="panel side" style="left:453px;top:35px">
    <svg class="photo" width="230" height="220" viewBox="0 0 230 220" role="img" aria-label="Collage: worker blowing insulation in an attic, thermal imaging camera, insulation removal">
      <defs>
        <linearGradient id="photoTop" x1="0" y1="0" x2="1" y2="1">
          <stop offset="0" stop-color="var(--photo-a)"/><stop offset=".5" stop-color="var(--photo-b)"/><stop offset="1" stop-color="var(--photo-c)"/>
        </linearGradient>
      </defs>
      <path d="M1,1 L199,1 C232,20 226,110 160,170 C130,198 100,214 74,219 L1,219 Z" fill="url(#photoTop)"/>
      <path d="M199,1 C232,20 226,110 160,170 C130,198 100,214 74,219" fill="none" stroke="var(--blue)" stroke-width="5"/>
    </svg>
    <div class="phone" style="left:366px;top:16px;font-size:21px"><span class="area">(559)</span> 318-2264</div>
    <div class="url" style="left:366px;top:41px;font-size:9.5px">www.<b>MarlowHeatworks</b>.com</div>
    <div class="tagline" style="left:300px;top:62px;font-size:11px">We fix high utility bills</div>
    <div class="brand-mark" style="left:300px;top:82px;width:52px;height:52px"></div>
    <div class="brand" style="left:302px;top:140px;font-size:19px">MARLOW<br>HEATWORKS</div>
    <ul class="services" style="left:391px;top:68px">
      <li>Insulation</li><li>Whole house fans</li><li>Window film</li><li>Insulation Removal</li><li>Thermal Imaging Inspections</li><li>Solar</li><li class="more">And more</li>
    </ul>
    <div class="badge" style="left:450px;top:173px" aria-label="Rating badge"></div>
    <div class="license" style="left:302px;top:201px">Lic#3859160</div>
  </section>
  <div class="brand-mark" style="left:1020px;top:250px;width:16px;height:16px"></div>
  <div class="brand" style="left:1020px;top:269px;font-size:7px">MARLOW<br>HEATWORKS</div>

  <!-- passenger side box, photo right -->
  <section class="panel side" style="left:262px;top:320px">
    <svg class="photo" width="510" height="220" viewBox="0 0 510 220" role="img" aria-label="Collage: worker blowing insulation in an attic, thermal imaging camera, insulation removal">
      <defs>
        <linearGradient id="photoBottom" x1="1" y1="0" x2="0" y2="1">
          <stop offset="0" stop-color="var(--photo-a)"/><stop offset=".5" stop-color="var(--photo-b)"/><stop offset="1" stop-color="var(--photo-c)"/>
        </linearGradient>
      </defs>
      <path d="M509,1 L311,1 C278,20 284,110 350,170 C380,198 410,214 436,219 L509,219 Z" fill="url(#photoBottom)"/>
      <path d="M311,1 C278,20 284,110 350,170 C380,198 410,214 436,219" fill="none" stroke="var(--blue)" stroke-width="5"/>
    </svg>
    <div class="phone" style="left:147px;top:18px;font-size:21px"><span class="area">(559)</span> 318-2264</div>
    <div class="url" style="left:147px;top:43px;font-size:9.5px">www.<b>MarlowHeatworks</b>.com</div>
    <ul class="services" style="left:25px;top:66px">
      <li>Insulation</li><li>Whole house fans</li><li>Window film</li><li>Insulation Removal</li><li>Thermal Imaging Inspections</li><li>Solar</li><li class="more">And more</li>
    </ul>
    <div class="tagline" style="left:200px;top:64px;font-size:11px">We fix high utility bills</div>
    <div class="brand-mark" style="left:200px;top:84px;width:52px;height:52px"></div>
    <div class="brand" style="left:200px;top:142px;font-size:19px">MARLOW<br>HEATWORKS</div>
    <div class="badge" style="left:25px;top:174px" aria-label="Rating badge"></div>
    <div class="license" style="left:200px;top:202px">Lic#3859160</div>
  </section>
  <div class="brand-mark" style="left:204px;top:532px;width:16px;height:16px"></div>
  <div class="brand" style="left:204px;top:551px;font-size:7px">MARLOW<br>HEATWORKS</div>

  <!-- rear door, contact version -->
  <section class="panel back-door" style="left:807px;top:341px">
    <div class="phone" style="left:122px;top:15px;font-size:18px"><span class="area">(559)</span> 318-2264</div>
    <div class="url" style="left:122px;top:37px;font-size:8.5px">www.<b>MarlowHeatworks</b>.com</div>
  </section>

</div>
</body>
</html>
```